Event Graphics for a Summer Camp for Middle School and High School Students

I need graphics designed for our summer camps event. These camps are for teenagers, 6-12th grades. Primary graphic design is for a 11x17 poster but will also need the images resized for:
-social media
-16x9 title slide
- a postcard size
Graphic should include the following:
-Main Title: KL Brightway presents . . . Summer Camp
-Dates: Ignite - June 3-7, High School - June 8-12, Middle School - June 22-26
-Register at KLBrightway.com
-Amberfold Retreat Center, Deadwood, SD
-For each camp, include name and headshot of speaker: Ignite: Mark Tolliver (black jacket photo), High: Danny Ruelas (hispanic man), Middle: Beckett Omari (tan shirt). Gave some options for headshots. Use what works best for cropping.
-Include KL Brightway logo
-Event Graphic should be attractive to teenagers. Open to ideas
My graphic design experience is limited. I will need help receiving the files I need in the various sizes. Thank you.

```html
<!DOCTYPE html>
<html lang="en">
<head>
<meta charset="utf-8">
<title>KL Brightway Summer Camps 2020</title>
<link rel="stylesheet" href="https://fonts.googleapis.com/css2?family=Courgette&family=Federo&family=Jost:wght@400&family=Montserrat+Alternates:ital,wght@1,800&family=Montserrat:ital,wght@1,800&family=Quicksand:wght@700&family=Rye&display=swap">
<style>
  :root {
    --night-purple: #3e1e44;
    --dusk-teal: #2f6a82;
    --forest-teal: #2a5f78;
    --lake-navy: #1d2c63;
    --deep-navy: #1a2f6e;
    --sun-orange: #f3823f;
    --sun-glow: #f6956a;
    --tent-magenta: #9a2f8e;
    --sky-cyan: #29c3f0;
    --camp-magenta: #9c3696;
    --plum-ink: #4b1a4b;
    --ribbon-ink: #13203f;
    --white: #ffffff;
  }
  * { margin: 0; padding: 0; box-sizing: border-box; }
  html, body { width: 777px; height: 1200px; overflow: hidden; background: var(--night-purple); }
  .poster {
    position: relative;
    width: 777px;
    height: 1200px;
    overflow: hidden;
    background: var(--night-purple);
  }
  .scene {
    position: absolute;
    left: 0; top: 0;
    width: 777px; height: 1200px;
    background:
      radial-gradient(ellipse 150px 70px at 150px 1020px, rgba(154,47,142,.85) 0, rgba(154,47,142,.55) 60%, rgba(154,47,142,0) 100%),
      radial-gradient(ellipse 150px 70px at 620px 1020px, rgba(154,47,142,.85) 0, rgba(154,47,142,.55) 60%, rgba(154,47,142,0) 100%),
      linear-gradient(180deg,
        rgba(0,0,0,0) 0,
        rgba(0,0,0,0) 450px,
        rgba(32,62,92,.55) 500px,
        rgba(26,48,86,.92) 560px,
        #2a4a7a 610px,
        #233c78 700px,
        #1d2d66 820px,
        #22397a 900px,
        #1e2f6c 960px,
        #243e80 1060px,
        #1a3470 1200px),
      linear-gradient(90deg,
        rgba(0,0,0,0) 0,
        rgba(0,0,0,0) 520px,
        rgba(70,150,190,.35) 620px,
        rgba(40,110,150,.45) 777px),
      radial-gradient(circle at 380px 520px, var(--sun-orange) 0, var(--sun-glow) 140px, rgba(246,149,106,.25) 178px, rgba(246,149,106,0) 200px),
      linear-gradient(180deg, var(--night-purple) 0, #3c2148 380px, #3a2a52 470px, var(--forest-teal) 560px);
  }
  .abs { position: absolute; text-align: center; white-space: nowrap; }
  .brand-name {
    left: 0; width: 777px; top: 88px;
    font-family: "Quicksand", sans-serif; font-weight: 700;
    font-size: 62px; line-height: 1; color: var(--sky-cyan);
  }
  .presents {
    left: 0; width: 777px; top: 180px;
    font-family: "Courgette", cursive; font-size: 36px; line-height: 1;
    color: var(--white);
  }
  .title-frame { position: absolute; left: 0; top: 0; }
  .title-summer {
    left: 0; width: 777px; top: 222px;
    font-family: "Quicksand", sans-serif; font-weight: 700;
    font-size: 84px; line-height: 1; color: var(--camp-magenta);
    letter-spacing: -1px;
  }
  .title-camps {
    left: 0; width: 777px; top: 280px;
    font-family: "Montserrat Alternates", sans-serif; font-style: italic; font-weight: 800;
    font-size: 68px; line-height: 1; color: var(--white);
    text-shadow: 0 0 10px rgba(120, 180, 255, .6);
  }
  .year {
    left: 0; width: 777px; top: 352px;
    font-family: "Montserrat", sans-serif; font-weight: 800;
    font-size: 42px; line-height: 1; color: var(--plum-ink); letter-spacing: 2px;
  }
  .camp-name {
    font-family: "Rye", serif; font-size: 40px; line-height: 1;
    color: var(--plum-ink);
    text-shadow: 0 0 12px rgba(255,255,255,.6), 0 0 3px rgba(255,255,255,.5);
  }
  .camp-dates {
    font-family: "Jost", sans-serif; font-weight: 400; font-size: 45px; line-height: 1;
    color: var(--white);
  }
  .speaker-name {
    font-family: "Montserrat", sans-serif; font-style: italic; font-weight: 800;
    font-size: 24px; line-height: 1; color: var(--ribbon-ink);
  }
  .graphics { position: absolute; left: 0; top: 0; }
  .venue {
    left: 33px; width: 714px; top: 1080px;
    font-family: "Federo", sans-serif; font-size: 33px; line-height: 1;
    color: var(--plum-ink);
  }
  .register {
    left: 0; width: 777px; top: 1136px;
    font-family: "Montserrat", sans-serif; font-style: italic; font-weight: 800;
    font-size: 40px; line-height: 1; color: var(--white);
    text-shadow: 0 0 12px var(--sky-cyan), 0 0 4px var(--sky-cyan);
  }
</style>
</head>
<body>
<main class="poster">
  <div class="scene" role="img" aria-label="Night camp landscape: orange setting sun behind a pine forest, a blue lake and rows of pink tents along the shore"></div>

  <div class="abs brand-name">KL Brightway</div>
  <div class="abs presents">present</div>

  <svg class="title-frame" width="777" height="460" viewBox="0 0 777 460" aria-hidden="true">
    <g fill="none" stroke="var(--white)" stroke-width="2">
      <polyline points="272,200 137,199 222,305"/>
      <polyline points="499,200 635,199 552,305"/>
      <polyline points="353,399 386,441 420,399"/>
    </g>
    <polygon points="288,345 490,345 478,374 490,404 288,404 300,374" fill="var(--sky-cyan)"/>
  </svg>

  <div class="abs title-summer">SUMMER</div>
  <div class="abs title-camps">camps</div>
  <div class="abs year">2020</div>

  <svg class="graphics" width="777" height="1200" viewBox="0 0 777 1200">
    <defs>
      <linearGradient id="toneStage" x1="0" y1="0" x2="0" y2="1">
        <stop offset="0" stop-color="#151632"/>
        <stop offset=".45" stop-color="#5a4550"/>
        <stop offset=".7" stop-color="#b98a78"/>
        <stop offset="1" stop-color="#2a2a30"/>
      </linearGradient>
      <linearGradient id="toneShirt" x1="0" y1="0" x2="0" y2="1">
        <stop offset="0" stop-color="#1a1a1a"/>
        <stop offset=".45" stop-color="#6a4a3c"/>
        <stop offset=".7" stop-color="#c49a86"/>
        <stop offset="1" stop-color="#e8e4e2"/>
      </linearGradient>
      <linearGradient id="toneLeaf" x1="0" y1="0" x2="0" y2="1">
        <stop offset="0" stop-color="#3b3a1c"/>
        <stop offset=".4" stop-color="#8a6a48"/>
        <stop offset=".7" stop-color="#c69a7c"/>
        <stop offset="1" stop-color="#d8cfc2"/>
      </linearGradient>
    </defs>

    <g fill="none" stroke="var(--white)" stroke-width="2">
      <polyline points="98,618 30,618 72,668"/>
      <polyline points="262,618 330,618 290,668"/>
      <polyline points="514,618 444,618 486,672"/>
      <polyline points="680,618 743,618 706,670"/>
      <polyline points="310,854 240,854 278,900"/>
      <polyline points="472,854 542,854 506,898"/>
    </g>

    <polygon role="img" aria-label="Photo of speaker Mark Tolliver in a black jacket holding a microphone" points="62,621 322,621 181,800" fill="url(#toneStage)"/>
    <polygon role="img" aria-label="Photo of speaker Danny Ruelas in a white shirt" points="475,621 733,621 593,800" fill="url(#toneShirt)"/>
    <polygon role="img" aria-label="Photo of speaker Beckett Omari in a tan shirt in front of leaves" points="255,857 528,857 390,1040" fill="url(#toneLeaf)"/>

    <g fill="var(--white)" stroke="var(--ribbon-ink)" stroke-width="1">
      <polygon points="160,792 204,792 181,812"/>
      <polygon points="570,792 616,792 593,812"/>
      <polygon points="367,1030 413,1030 390,1049"/>
    </g>

    <g fill="var(--sky-cyan)">
      <polygon points="76,741 286,739 274,767 288,797 74,795 86,768"/>
      <polygon points="489,741 701,739 689,767 703,797 487,795 499,768"/>
      <polygon points="277,978 504,976 492,1004 506,1034 275,1032 287,1005"/>
    </g>

    <polygon points="33,1072 747,1072 736,1098 747,1126 33,1126 44,1099" fill="var(--white)"/>
  </svg>

  <div class="abs camp-name" style="left:56px;width:258px;top:518px;">IGNITE</div>
  <div class="abs camp-dates" style="left:48px;width:272px;top:563px;">JUNE 03-07</div>
  <div class="abs speaker-name" style="left:80px;width:204px;top:756px;">Mark Tolliver</div>

  <div class="abs camp-name" style="left:474px;width:238px;top:518px;">HIGH</div>
  <div class="abs camp-dates" style="left:466px;width:258px;top:563px;">JUNE 8-12</div>
  <div class="abs speaker-name" style="left:493px;width:204px;top:756px;">Danny Ruelas</div>

  <div class="abs camp-name" style="left:240px;width:302px;top:772px;">MIDDLE</div>
  <div class="abs camp-dates" style="left:240px;width:302px;top:813px;">JUNE 22-26</div>
  <div class="abs speaker-name" style="left:280px;width:220px;top:993px;">Beckett Omari</div>

  <div class="abs venue">Amberfold Retreat Center, Deadwood, SD</div>
  <div class="abs register">Register @ KLBrightway.com</div>
</main>
</body>
</html>
```